Local snack brand needs a WordPress theme design

We need a custom WordPress theme for a new Australian snack company called Crunchwell. Based in Coffs Harbour, we create functional food snacks using local bananas and other produce. The theme should reflect our community-first philosophy and local roots, featuring an aerial banner of the region’s banana plantations and images of growers harvesting bananas.
The design should include layouts for:
1. Bio pages (profile photo and blurb)
2. Product pages (packaging, nutrition information panel, ingredients, 3. product description, health claim badges like “source of fibre” and “good source of potassium,” and awards)
4. Where to Buy page (interactive map, market stall imagery)
5. Blog posts (feature image, paragraph, quotes)
The final theme should use Crunchwell’s vector logo in the header (without text), and Crunchwell name (in brand font) in the footer. Should be modern, responsive design (mobile first). It should have a grass roots feel, be clean and feel good, leverage the brand colours, but still feel professional (to reflect a horticulturist and nutritionist), and be flexible for future updates. The successful design needs to be delivered as an installable theme in ZIP archive.
Please visit our website and read our pages to get a feel for "us". See https://crunchwell-example.au/
1 week extension for the 3 finalists to respond to feedback and make their final submissions before awarding 1st, 2nd and 3rd.
Local, health-conscious, athletes, busy parents, active minds
Food wholesaler, health & nutrition, agribusiness / local produce
- Galano Grotesque Bold

```html
<!DOCTYPE html>
<html lang="en">
<head>
<meta charset="utf-8">
<title>Crunchwell – Goodness Grown in Coffs Harbour</title>
<link href="https://fonts.googleapis.com/css2?family=Poppins:wght@400;500;600;700&display=swap" rel="stylesheet">
<style>
:root{
  --green:#5f9535;
  --green-deep:#5a8d37;
  --green-text:#6a9a3f;
  --ink:#1b1b1b;
  --muted:#555;
  --grey-bg:#ececec;
  --white:#fff;
  --topbar:#111;
  --footer:#1e2822;
}
*{box-sizing:border-box;margin:0;padding:0}
html,body{width:1200px;height:4769px;overflow:hidden}
body{font-family:"Poppins",sans-serif;color:var(--ink);background:var(--white);position:relative}

/* top bar */
.topbar{position:absolute;top:0;left:0;width:1200px;height:28px;background:var(--topbar);color:#fff;font-size:10px}
.topbar .social{position:absolute;left:72px;top:8px;display:flex;gap:21px}
.dot{width:12px;height:12px;border-radius:50%;background:#fff;display:block}
.topbar .lang{position:absolute;left:902px;top:7px}
.topbar .login{position:absolute;left:1028px;top:7px}

/* nav */
.nav{position:absolute;top:28px;left:0;width:1200px;height:64px;background:#fff}
.brand{position:absolute;left:70px;top:20px;display:flex;align-items:center;gap:8px;font-weight:700;font-size:18px;color:var(--green)}
.brand .mark{width:14px;height:14px;border-radius:50%;background:var(--green)}
.menu-item{position:absolute;top:24px;font-size:10px;font-weight:500;text-transform:uppercase;white-space:nowrap}
.menu-item.active::before{content:"";position:absolute;left:-2px;right:-2px;top:-24px;height:3px;background:var(--green)}
.icon-btn{position:absolute;top:18px;width:26px;height:26px;border:1.5px solid #333;border-radius:50%}
.btn-contact{position:absolute;left:1007px;top:14px;width:117px;height:34px;border-radius:17px;background:var(--green);color:#fff;font-size:11px;font-weight:500;display:flex;align-items:center;justify-content:center}

/* hero */
.hero{position:absolute;top:92px;left:0;width:1200px;height:640px;background:radial-gradient(ellipse at 60% 35%,#8a9a4a 0%,#3f5a24 35%,#1f2f14 75%,#172410 100%)}
.hero-inner{position:absolute;left:0;width:1200px;text-align:center;color:#fff}
.hero .eyebrow{top:193px;font-size:12px}
.hero h1{top:208px;font-size:46px;line-height:53px;font-weight:700}
.hero p{top:322px;font-size:12px;line-height:20px}
.btn{display:flex;align-items:center;justify-content:center;border-radius:17px;font-size:10px;font-weight:500;text-transform:uppercase}
.btn-shop{position:absolute;left:476px;top:375px;width:117px;height:32px;background:var(--green);color:#fff}
.btn-ghost{position:absolute;left:607px;top:375px;width:117px;height:32px;border:1.5px solid #fff;color:#fff}

/* welcome */
.welcome{position:absolute;top:732px;left:0;width:1200px;height:666px;background:#fff}
.welcome .photo{position:absolute;left:0;top:80px;width:722px;height:586px;background:linear-gradient(120deg,#f4f4f2 0%,#6c7a3e 30%,#4a5a2c 55%,#8a6a4a 75%,#f3f3f1 100%)}
.welcome h2{position:absolute;left:733px;top:170px;font-size:40px;line-height:42px;font-weight:700}
.welcome .lead{position:absolute;left:733px;top:275px;width:350px;font-size:11.5px;line-height:17px;color:var(--muted)}
.welcome .body{position:absolute;left:733px;top:325px;width:350px;font-size:11.5px;line-height:17px;color:var(--muted)}
.btn-outline{position:absolute;border:2px solid #222;color:#111;border-radius:24px;background:#fff;font-weight:600;font-size:10.5px;text-transform:uppercase;display:flex;align-items:center;justify-content:center}

/* products */
.products{position:absolute;top:1398px;left:0;width:1200px;height:565px;background:var(--grey-bg)}
.section-title{position:absolute;left:0;width:1200px;text-align:center;font-weight:700;font-size:38px}
.product{position:absolute;top:182px;width:217px;text-align:center}
.product .disc{width:217px;height:217px;border-radius:50%}
.product span{display:block;margin-top:30px;font-size:24px;font-weight:600;color:var(--green-text)}

/* ingredients */
.ingredients{position:absolute;top:1963px;left:0;width:1200px;height:1074px;background:#fff}
.ingredients .sub{position:absolute;left:0;width:1200px;top:138px;text-align:center;font-size:11px;line-height:19px;color:#333}
.card{position:absolute;width:245px;height:366px;background:#fff;border-radius:18px;box-shadow:0 6px 16px rgba(0,0,0,.09);overflow:hidden}
.card .img{height:191px}
.card h3{margin:28px 30px 0;font-size:13px;line-height:18px;font-weight:700;text-transform:uppercase}
.card p{margin:6px 30px 0;font-size:10.5px;line-height:17px;color:#444}
.card .more{display:block;margin:6px 30px 0;font-size:12px;font-weight:600}

/* where to buy */
.wtb{position:absolute;top:3037px;left:0;width:1200px;height:528px;background:var(--green-deep);color:#fff;overflow:hidden}
.wtb .scene{position:absolute;left:556px;top:0;width:644px;height:528px;border-radius:300px 0 0 300px/264px 0 0 264px;background:linear-gradient(180deg,#b9cbd6 0%,#dfe6ea 30%,#3e5d2c 55%,#6f9a45 75%,#7fa752 100%)}
.wtb .kicker{position:absolute;left:96px;top:141px;font-size:13px;font-weight:600}
.wtb h2{position:absolute;left:94px;top:160px;font-size:35px;font-weight:700;text-transform:uppercase}
.wtb .text{position:absolute;left:96px;top:208px;width:400px;font-size:11px;line-height:17px}
.wtb ul{position:absolute;left:96px;top:283px;list-style:none;font-size:11px;line-height:17px}
.wtb li{display:flex;align-items:center;gap:6px}
.wtb li.indent{padding-left:12px}
.btn-white{position:absolute;left:94px;top:367px;width:128px;height:35px;border-radius:18px;background:#fff;color:#222;font-size:11px;font-weight:500;display:flex;align-items:center;justify-content:center}

/* community */
.community{position:absolute;top:3565px;left:0;width:1200px;height:778px;background:#fff}
.post{position:absolute;top:185px;width:280px;height:404px;background:#fff;border-radius:18px;box-shadow:0 6px 16px rgba(0,0,0,.09);overflow:hidden}
.post .img{height:231px;position:relative}
.post .date{position:absolute;left:40px;bottom:-10px;background:var(--green);color:#fff;font-size:9px;padding:4px 12px;border-radius:10px}
.post h3{margin:38px 40px 0;font-size:14px;line-height:20px;font-weight:600}
.post p{margin:14px 40px 0;font-size:11px;line-height:16px;color:#666}
.post .more{display:block;margin:14px 40px 0;font-size:9px;font-weight:600;text-decoration:underline}

/* footer */
.footer{position:absolute;top:4343px;left:0;width:1200px;height:426px;background:var(--footer);color:#fff}
.footer .fbrand{position:absolute;left:128px;top:168px;font-size:23px;font-weight:700;letter-spacing:.5px}
.footer .news{position:absolute;left:128px;top:204px;width:260px;font-size:11px;line-height:17px}
.footer .email{position:absolute;left:128px;top:252px;width:262px;height:38px;border-radius:19px;background:#2b3630;font-size:11px;padding:11px 22px;color:#ddd}
.footer .go{position:absolute;left:348px;top:252px;width:38px;height:38px;border-radius:50%;background:var(--green);font-size:11px;display:flex;align-items:center;justify-content:center}
.footer h4{position:absolute;top:125px;font-size:17px;font-weight:600}
.footer .links{position:absolute;left:531px;top:162px;list-style:none;font-size:12px;line-height:22.5px}
.footer .contact{position:absolute;left:807px;top:162px;list-style:none;font-size:12px;line-height:22px}
.footer .contact li{display:flex;align-items:center;gap:8px}
.footer .contact .name{font-weight:600;font-size:13px}
.footer .copy{position:absolute;left:128px;top:390px;font-size:11px}
.footer .fsocial{position:absolute;left:962px;top:387px;display:flex;gap:8px}
.footer .fsocial i{width:22px;height:22px;border-radius:50%;border:1.5px solid #fff;display:block}
.footer .top{position:absolute;left:1130px;top:360px;width:32px;height:32px;border-radius:50%;background:var(--green)}
</style>
</head>
<body>

<header class="topbar">
  <div class="social"><i class="dot"></i><i class="dot"></i><i class="dot"></i><i class="dot"></i><i class="dot"></i></div>
  <span class="lang">English (US) ▾</span>
  <span class="login">Client's Log in</span>
</header>

<nav class="nav">
  <div class="brand"><span class="mark"></span>Crunchwell</div>
  <span class="menu-item active" style="left:350px">Home</span>
  <span class="menu-item" style="left:413px">Our Ingredients</span>
  <span class="menu-item" style="left:535px">Our Snacks</span>
  <span class="menu-item" style="left:635px">Our Story</span>
  <span class="menu-item" style="left:726px">Where to Buy</span>
  <span class="menu-item" style="left:833px">Blog</span>
  <span class="icon-btn" style="left:886px"></span>
  <span class="icon-btn" style="left:927px"></span>
  <span class="icon-btn" style="left:966px"></span>
  <span class="btn-contact">CONTACT US</span>
</nav>

<section class="hero">
  <div role="img" aria-label="Aerial view of banana plantations in the Coffs Harbour hinterland" style="position:absolute;inset:0"></div>
  <div class="hero-inner eyebrow">Welcome to Crunchwell</div>
  <h1 class="hero-inner">Goodness Grown in<br>Coffs Harbour</h1>
  <p class="hero-inner">Crunchwell creates wholesome, functional snacks using locally grown<br>bananas and fresh produce. Healthy fuel for active minds and busy lives.</p>
  <span class="btn btn-shop">Shop Snacks</span>
  <span class="btn btn-ghost">Our Ingredients</span>
</section>

<section class="welcome">
  <div class="photo" role="img" aria-label="Grower carrying a freshly harvested bunch of green bananas"></div>
  <h2>Welcome to<br>Crunchwell</h2>
  <p class="lead">The science of functional snacking — grown, crafted and shared on the Coffs Coast.</p>
  <p class="body">We're Sam &amp; Theo — a grower and a nutritionist — combining our love of real food and sustainable practice to create something a little different. Crunchwell is where fresh thinking meets rescued produce, and where small batches are made with big purpose.</p>
  <span class="btn-outline" style="left:733px;top:440px;width:139px;height:46px">Our History</span>
</section>

<section class="products">
  <h2 class="section-title" style="top:92px">Our Products</h2>
  <div class="product" style="left:123px"><div class="disc" role="img" aria-label="Coconut and bananas" style="background:radial-gradient(circle at 55% 55%,#f1d36a,#c9a779 55%,#b08a5e)"></div><span>Coco Crunch</span></div>
  <div class="product" style="left:361px"><div class="disc" role="img" aria-label="Banana slices with cinnamon sticks" style="background:radial-gradient(circle,#f3ede4,#ddd3c4 70%,#cbbfae)"></div><span>Cinna Bite</span></div>
  <div class="product" style="left:599px"><div class="disc" role="img" aria-label="Coffee beans and banana slices" style="background:radial-gradient(circle at 70% 50%,#e9d6a0,#6b4024 50%,#3a2214)"></div><span>Banoffee</span></div>
  <div class="product" style="left:838px"><div class="disc" role="img" aria-label="Bananas with a bowl of macadamias" style="background:radial-gradient(circle at 35% 45%,#e8c24c,#7a5434 55%,#3f2a1c)"></div><span>Maca Bite</span></div>
</section>

<section class="ingredients">
  <h2 class="section-title" style="top:82px">Our Ingredients</h2>
  <p class="sub">At Crunchwell, what goes into our snacks matters as much as what doesn't.<br>Every batch we make starts with real</p>

  <article class="card" style="left:217px;top:207px">
    <div class="img" role="img" aria-label="Bunch of bananas on the plant" style="background:linear-gradient(160deg,#a9c25a,#5f8a2e 60%,#3a5a1e)"></div>
    <h3>Bananas<br>Local, Naturally Sweet</h3>
    <p>Our hero ingredient. We source Cavendish, Ducasse and Lady Finger bananas grown right here in the Coffs Harbour region.....</p>
    <span class="more">View More</span>
  </article>
  <article class="card" style="left:470px;top:207px">
    <div class="img" role="img" aria-label="Macadamia nuts on a wooden table" style="background:linear-gradient(160deg,#8a5a36,#5a3a22 60%,#3e2818)"></div>
    <h3>Macadamias -<br>Grown in Northern NSW</h3>
    <p>Rich in healthy fats, protein, and minerals, macadamias help create snacks that are satisfying and sustaining</p>
    <span class="more">View More</span>
  </article>
  <article class="card" style="left:724px;top:207px">
    <div class="img" role="img" aria-label="Green coconuts on a palm" style="background:linear-gradient(160deg,#c9d28a,#7f9a46 55%,#4a6226)"></div>
    <h3>Coconut-A Tropical<br>Partner</h3>
    <p>Our coconut is carefully selected for purity and minimal processing, keeping it as close to the source as possible</p>
    <span class="more">View More</span>
  </article>

  <article class="card" style="left:217px;top:593px">
    <div class="img" role="img" aria-label="Cup overflowing with roasted coffee beans" style="background:linear-gradient(160deg,#6a4128,#3c2416 60%,#24160c)"></div>
    <h3>Coffee-Small-Batch<br>Roasted, Big on Flavour</h3>
    <p>Perfect for athletes and active minds, this blend combines the slow-release carbs of banana with the focus-enhancing power ..</p>
    <span class="more">View More</span>
  </article>
  <article class="card" style="left:470px;top:593px">
    <div class="img" role="img" aria-label="Fresh raspberries, strawberries and blueberries" style="background:linear-gradient(160deg,#c43a4e,#7a3a6a 50%,#3d4a7a)"></div>
    <h3>Berries-Blueberries<br>and More</h3>
    <p>Packed with antioxidants and vibrant flavour, our berry-based snacks like Berry Bites and Blue Chia Rolls turn surplus ..</p>
    <span class="more">View More</span>
  </article>
  <article class="card" style="left:724px;top:593px">
    <div class="img" role="img" aria-label="Native botanical leaves and herbs" style="background:linear-gradient(160deg,#8a8e6a,#5e6a40 55%,#3f4a2a)"></div>
    <h3>Native Botanicals<br>A Taste of Place</h3>
    <p>Where we can, we use Australian native flavours like lemon myrtle and finger lime. These ingredients are sustainably harvested</p>
    <span class="more">View More</span>
  </article>
</section>

<section class="wtb">
  <div class="scene" role="img" aria-label="Weekend market stalls on the grass beside tall pine trees"></div>
  <div class="kicker">Seaside Growers Markets</div>
  <h2>Where to Buy</h2>
  <p class="text">Find us by the beach every Sunday<br>You can catch Crunchwell in person every week at the Seaside Growers Markets- a beautiful makers and growers market held at the Marina Foreshore in Coffs Harbour.</p>
  <ul>
    <li><svg width="8" height="10" viewBox="0 0 8 10"><path d="M4 0a4 4 0 0 1 4 4c0 3-4 6-4 6S0 7 0 4a4 4 0 0 1 4-4z" fill="#fff"/></svg>Seaside Growers Markets</li>
    <li class="indent">Marina Foreshore, Coffs Harbour</li>
    <li><svg width="9" height="9" viewBox="0 0 9 9"><circle cx="4.5" cy="4.5" r="4.5" fill="#fff"/><path d="M4.5 2v2.7h2" stroke="#5a8d37" stroke-width="1" fill="none"/></svg>Every Sunday, 8am–2pm</li>
    <li><svg width="9" height="9" viewBox="0 0 9 9"><path d="M0 8h9M1 6c2-3 5-3 7 0" stroke="#fff" stroke-width="1.3" fill="none"/></svg>Beachside, all-weather, all abilities</li>
  </ul>
  <span class="btn-white">READ MORE</span>
</section>

<section class="community">
  <h2 class="section-title" style="top:100px">From the Community</h2>

  <article class="post" style="left:152px">
    <div class="img" role="img" aria-label="Farmer harvesting bananas in a plantation" style="background:linear-gradient(160deg,#9ab860,#4f7a2a 60%,#2f4a1a)"><span class="date">25-05-2025</span></div>
    <h3>5 Benefits of Bananas<br>for Busy Parents</h3>
    <p>Proin gravida nibh vel velit auctor aliquet aenean sollicitudin..</p>
    <span class="more">LEARN MORE</span>
  </article>
  <article class="post" style="left:455px">
    <div class="img" role="img" aria-label="Banana dessert with ice cream" style="background:linear-gradient(160deg,#f1e8d6,#d7b073 50%,#6a4526)"><span class="date">25-05-2025</span></div>
    <h3>Why Functional Snacks<br>Are the Future of Food</h3>
    <p>Proin gravida nibh vel velit auctor aliquet aenean sollicitudin..</p>
    <span class="more">LEARN MORE</span>
  </article>
  <article class="post" style="left:757px">
    <div class="img" role="img" aria-label="Smiling grower holding a bunch of bananas" style="background:linear-gradient(160deg,#b6c98a,#6f8a4e 55%,#4a5e34)"><span class="date">25-05-2025</span></div>
    <h3>Meet Our Growers: Life on<br>the Coffs Coast</h3>
    <p>Proin gravida nibh vel velit auctor aliquet aenean sollicitudin..</p>
    <span class="more">LEARN MORE</span>
  </article>

  <span class="btn-outline" style="left:526px;top:663px;width:138px;height:46px">View All Blog</span>
</section>

<footer class="footer">
  <div class="fbrand">CRUNCHWELL</div>
  <p class="news">Sign up our newsletter to get Healthy tips &amp; latest updates!</p>
  <div class="email">Email Address</div>
  <span class="go">GO</span>

  <h4 style="left:531px">Quick Links</h4>
  <ul class="links"><li>Home</li><li>About Us</li><li>Products</li><li>Where to Buy</li><li>Blog</li><li>Contact Us</li></ul>

  <h4 style="left:807px">Contact Details</h4>
  <ul class="contact">
    <li class="name">CRUNCHWELL</li>
    <li><svg width="8" height="10" viewBox="0 0 8 10"><path d="M4 0a4 4 0 0 1 4 4c0 3-4 6-4 6S0 7 0 4a4 4 0 0 1 4-4z" fill="#6a9a3f"/></svg>Seaside Growers Markets</li>
    <li style="padding-left:16px">Marina Foreshore, Coffs Harbour</li>
    <li><svg width="9" height="9" viewBox="0 0 9 9"><circle cx="4.5" cy="4.5" r="4.5" fill="#6a9a3f"/></svg>Every Sunday, 8am-2pm</li>
    <li><svg width="9" height="9" viewBox="0 0 9 9"><path d="M0 8h9M1 6c2-3 5-3 7 0" stroke="#6a9a3f" stroke-width="1.3" fill="none"/></svg>Beachside, all-weather, all abilities</li>
    <li><svg width="10" height="8" viewBox="0 0 10 8"><rect width="10" height="8" rx="1" fill="#6a9a3f"/><path d="M0 1l5 3 5-3" stroke="#1e2822" fill="none"/></svg>@crunchwell.au</li>
  </ul>

  <span class="top"></span>
  <p class="copy">Copyright 2025 Crunchwell. All Rights Reserved.</p>
  <div class="fsocial"><i></i><i></i><i></i><i></i></div>
</footer>

</body>
</html>
```